New Business Card for Innovative Tool Company

We need a new design of business card for our florida based tool manufacturing company. I will attach 2 files that we use for our logo, use whichever you feel works best for the card. Main colours are as per logo, and we can use different shades of black/white/grey for the background.

Contact Information for Business Card

Name/Jobtitle/cell
Corvalen Tools
Suite 212c
4316 Marrowdale Pkw
Orlando, FL32847
USA
name@corvaleninc.example
www.corvaleninc.example

Font styles to use
Sans Serif

Colors

Designer to choose colors to be used in the design.

Requirements
Must have
• Icons for Plazaro, Chirpet, Snapvale, Findlo & Vidstream

```html
<!DOCTYPE html>
<html lang="en">
<head>
<meta charset="utf-8">
<title>Corvalen Tools – Business Card</title>
<link rel="stylesheet" href="https://fonts.googleapis.com/css2?family=Lato:wght@400;700;900&display=swap">
<style>
  :root {
    --page: #ffffff;
    --card: #282828;
    --yellow: #f7ea3a;
    --text-light: #e4e4e4;
    --text-soft: #bdbdbd;
    --emblem-fill: #6a6a6a;
    --emblem-ring: #d9d9d9;
  }
  * { margin: 0; padding: 0; box-sizing: border-box; }
  html, body {
    width: 1200px; height: 1200px; overflow: hidden;
    background: var(--page);
    font-family: "Lato", sans-serif;
  }
  .canvas { position: relative; width: 1200px; height: 1200px; }
  .card {
    position: absolute; left: 246px; width: 707px; height: 403px;
    background: var(--card); border-radius: 32px; overflow: hidden;
  }
  .card-front { top: 138px; }
  .card-back { top: 646px; }

  /* Front */
  .front-emblem {
    position: absolute; left: 266px; top: 114px; width: 176px; height: 176px;
    border-radius: 50%; background: var(--emblem-fill);
    border: 3px solid var(--emblem-ring);
    display: flex; align-items: center; justify-content: center;
  }
  .front-emblem .brand-name {
    color: var(--yellow); font-weight: 900; font-size: 19px;
  }
  .social-row {
    position: absolute; left: 0; right: 0; top: 359px;
    display: flex; justify-content: center; gap: 12px;
  }
  .social-item {
    display: flex; align-items: center; gap: 4px;
    color: var(--text-soft); font-size: 10px;
  }
  .social-dot { width: 8px; height: 8px; border-radius: 50%; background: var(--text-soft); }

  /* Back */
  .name-tab {
    position: absolute; left: 0; top: 138px; width: 23px; height: 112px;
    background: var(--yellow); border-radius: 0 24px 24px 0;
  }
  .person-name {
    position: absolute; left: 38px; top: 168px;
    color: var(--yellow); font-size: 29px; font-weight: 700; line-height: 1;
  }
  .person-title {
    position: absolute; left: 38px; top: 206px;
    color: var(--text-light); font-size: 17px; font-weight: 700; line-height: 1;
  }
  .contact-list { position: absolute; left: 40px; top: 298px; list-style: none; }
  .contact-item {
    display: flex; align-items: center; gap: 10px; height: 25px;
    color: var(--text-light); font-size: 17px;
  }
  .contact-item svg { width: 14px; height: 14px; flex: none; }
  .accent { color: var(--yellow); }
  .brand-block {
    position: absolute; left: 400px; top: 40px; width: 235px;
    display: flex; flex-direction: column; align-items: center; gap: 22px;
  }
  .brand-circle {
    width: 100px; height: 100px; border-radius: 50%;
    border: 1.5px solid #6f6a35;
  }
  .brand-block .brand-name {
    color: var(--yellow); font-weight: 900; font-size: 30px; white-space: nowrap;
  }
  .address {
    position: absolute; left: 382px; top: 316px;
    color: var(--text-light); font-size: 17px; line-height: 28px;
  }
</style>
</head>
<body>
<main class="canvas">
  <section class="card card-front">
    <div class="front-emblem"><span class="brand-name">Corvalen Tools</span></div>
    <ul class="social-row">
      <li class="social-item"><span class="social-dot"></span>Plazaro</li>
      <li class="social-item"><span class="social-dot"></span>Findlo</li>
      <li class="social-item"><span class="social-dot"></span>Snapvale</li>
      <li class="social-item"><span class="social-dot"></span>Vidstream</li>
      <li class="social-item"><span class="social-dot"></span>Chirpet</li>
    </ul>
  </section>

  <section class="card card-back">
    <div class="name-tab"></div>
    <h1 class="person-name">Daniel Hartwell</h1>
    <p class="person-title">President</p>

    <ul class="contact-list">
      <li class="contact-item">
        <svg viewBox="0 0 24 24" aria-hidden="true"><path fill="#f7ea3a" d="M6.6 10.8a15 15 0 0 0 6.6 6.6l2.2-2.2c.3-.3.7-.4 1-.2 1.1.4 2.3.6 3.6.6.6 0 1 .4 1 1V20c0 .6-.4 1-1 1A17 17 0 0 1 3 4c0-.6.4-1 1-1h3.5c.6 0 1 .4 1 1 0 1.3.2 2.5.6 3.6.1.3 0 .7-.2 1z"/></svg>
        (08) 5550 4172
      </li>
      <li class="contact-item">
        <svg viewBox="0 0 24 24" aria-hidden="true"><path fill="#f7ea3a" d="M2 5h20v14H2z"/><path fill="none" stroke="#282828" stroke-width="2" d="M2 5l10 8 10-8M2 19l7-7M22 19l-7-7"/></svg>
        name@corvaleninc.example
      </li>
      <li class="contact-item">
        <svg viewBox="0 0 24 24" aria-hidden="true"><g fill="none" stroke="#bdb25a" stroke-width="1.8"><circle cx="12" cy="12" r="9.5"/><ellipse cx="12" cy="12" rx="4" ry="9.5"/><path d="M2.5 12h19M4 7h16M4 17h16"/></g></svg>
        <span>www.<span class="accent">corvaleninc</span>.example</span>
      </li>
    </ul>

    <div class="brand-block">
      <div class="brand-circle"></div>
      <span class="brand-name">Corvalen Tools</span>
    </div>

    <address class="address" style="font-style:normal">
      Suite 212c, 4316 Marrowdale Pkw<br>
      Orlando, FL32847, USA
    </address>
  </section>
</main>
</body>
</html>
```